CONTACT US Page and design for website

We need a contact us page for our website. We would like it to have a message area, a map, our information, etc.

Please see the text attachment for what we are looking for. We need to have something that is creative and interesting, modern and professional.

We believe that a contact US page should be very creative because everyone clicks that to contact us. We want it to be super professional, attention grabbing, pleasing to the eye.

PLEASE KEEP THE HEADER AND FOOTER THE SAME, ONLY THE ACTUAL CONTACT US PAGE NEEDS TO BE WORKED ON. THANKS!
We are excited to work with designers for this project.

Target Market(s)

Clients in technology business

Industry/Entity Type

Information Technology

Number of Pages Required

1 page

Font styles to use
Serif

Requirements
Must have
• CHECK THE TEXT ATTACHMENT PLEASE
• Must stay within our design colors and theme.
Nice to have
• see attachment
Should not have
• it should be special

```html
<!DOCTYPE html>
<html lang="en">
<head>
<meta charset="utf-8">
<title>Contact Us – Quellory</title>
<link href="https://fonts.googleapis.com/css2?family=Arimo:wght@400;700&display=swap" rel="stylesheet">
<style>
:root{
  --teal:#3dd0c1;
  --teal-dark:#2fb4a8;
  --ink:#333;
  --muted:#666;
  --line:#d8d8d8;
  --card:#ededed;
  --footer:#a7a7a7;
  --footer-dark:#9b9b9b;
  --white:#fff;
}
*{box-sizing:border-box;margin:0;padding:0}
html,body{width:1061px;height:1200px;overflow:hidden;background:var(--white);font-family:"Arimo",Arial,sans-serif;color:var(--ink)}
.page{position:relative;width:1061px;height:1200px}
.abs{position:absolute}

/* header */
.account-pill{left:887px;top:0;width:120px;height:21px;background:#a9a9a9;border-radius:0 0 14px 14px;display:flex;font-size:7px;color:#555}
.account-pill span{flex:1;text-align:center;line-height:21px}
.account-pill span+span{border-left:1px solid #c8c8c8}
.brand{left:56px;top:14px;display:flex;align-items:center;gap:10px}
.brand-mark{width:44px;height:44px;background:var(--teal);border-radius:50%}
.brand-name{font-size:24px;letter-spacing:1px;color:var(--teal-dark);font-weight:400}
.head-contact{left:818px;top:28px;display:flex;align-items:center;gap:8px;font-size:9px;color:#555}
.round-icon{width:26px;height:26px;border-radius:50%;border:1px solid #ddd;display:flex;align-items:center;justify-content:center}
.head-phone{font-size:12px;color:#333}
.nav{left:61px;top:73px;display:flex;gap:16.5px;font-size:8.6px;color:#444}
.header-rule{left:0;top:62px;width:1061px;height:1px;background:#e6e6e6}
.search{left:817px;top:69px;width:143px;height:21px;border:1px solid #ccc;border-radius:11px;font-size:7px;color:#555;padding:6px 18px}
.search svg{position:absolute;right:8px;top:5px}
.cart{left:972px;top:67px;width:25px;height:25px;border:1px solid #ccc;border-radius:50%;display:flex;align-items:center;justify-content:center}
.crumb{left:0;top:94px;width:1061px;height:24px;background:linear-gradient(90deg,#2bb7ae,var(--teal) 60%,#36c6b9);font-size:8px;font-weight:700;color:#0f3b38;padding:8px 62px}
.crumb b{color:var(--white)}

.page-title{left:0;top:136px;width:1061px;text-align:center;font-size:13px;letter-spacing:.5px;font-weight:400}
.page-title::after{content:"";display:block;width:20px;height:1px;background:#777;margin:7px auto 0}

/* map */
.map{left:0;top:174px;width:1061px;height:301px;background:linear-gradient(180deg,#e9e9e9,#e2e2e2);border-top:1px solid #d6d6d6;border-bottom:1px solid #d6d6d6}
.map-river{left:0;top:198px;width:1061px;height:9px;background:#a8cbf2}
.map-popup{left:428px;top:285px;width:153px;height:67px;background:var(--white);box-shadow:0 1px 4px rgba(0,0,0,.25);text-align:center;font-size:7px;line-height:11px;padding-top:9px}
.map-popup strong{display:block;margin-bottom:4px;font-size:7.2px}
.map-pin{left:497px;top:358px}
.map-pin-label{left:510px;top:378px;font-size:6.5px;font-weight:700;color:#b0202a}

/* hours */
.section-head{font-size:11.5px;letter-spacing:.3px;font-weight:400}
.section-head::after{content:"";display:block;width:20px;height:1px;background:var(--teal);margin-top:6px}
.hours{left:54px;top:503px;width:340px}
.hours-list{margin-top:14px}
.hour-row{display:flex;align-items:center;font-size:10px;height:22px;color:#444}
.hour-row svg{margin-right:9px}
.dots{border-bottom:1px dashed #999;height:0;margin:0 4px;flex:0 0 auto;transform:translateY(1px)}
.hours-note{margin-top:6px;font-size:9.5px;display:flex;align-items:center;gap:6px;color:#444}
.badge24{width:20px;height:20px;border-radius:50%;border:2px solid var(--teal);font-size:7px;color:var(--teal);display:flex;align-items:center;justify-content:center;font-weight:700}
.connect{left:54px;top:684px}
.social-dark{display:flex;gap:3px;margin-top:20px}
.social-dark span{width:19px;height:19px;border-radius:50%;background:#444}

/* form */
.touch{left:538px;top:503px;width:470px}
.field-row{display:flex;gap:10px;margin-top:22px}
.field label,.message label{display:block;font-size:7.5px;letter-spacing:.5px;margin-bottom:4px}
.field label i,.message label i{color:#c0392b;font-style:normal}
.field .box{width:150px;height:27px;border:1.5px solid #ccc}
.message{margin-top:17px}
.message .box{width:470px;height:71px;border:1.5px solid #ccc}
.send{margin-top:25px;width:83px;height:30px;background:var(--teal);color:var(--white);font-size:8px;font-weight:700;letter-spacing:.5px;display:flex;align-items:center;justify-content:center}

/* inquiry cards */
.card{top:783px;width:242px;height:83px;background:var(--card);border:1px solid #d5d5d5;display:flex}
.card-icon{width:100px;display:flex;align-items:center;justify-content:center}
.card-body{padding-top:12px}
.card-body h3{font-size:9px;font-weight:700;letter-spacing:.3px;margin-bottom:7px}
.card-line{display:flex;align-items:center;gap:10px;font-size:8.5px;color:#444;height:22px}
.dot-icon{width:18px;height:18px;border-radius:50%;background:#555;display:flex;align-items:center;justify-content:center}

/* footer */
.footer{left:0;top:910px;width:1061px;height:179px;background:var(--footer);color:var(--white)}
.footer-about{width:480px;margin:13px auto 0;text-align:center;font-size:9px;line-height:12.3px}
.footer-rule{width:520px;height:1px;background:#b8b8b8;margin:9px auto 0}
.footer-contact{left:332px;top:79px;display:flex;font-size:9px;line-height:12px}
.footer-contact div{display:flex;gap:8px}
.footer-links{left:276px;top:124px;display:flex;font-size:10px}
.footer-links .sub{font-size:6px;line-height:8.8px;text-align:center;margin-top:3px}
.footer-base{left:0;top:1089px;width:1061px;height:111px;background:var(--footer-dark);color:var(--white)}
.social-outline{display:flex;gap:9px;justify-content:center;margin-top:12px}
.social-outline span{width:24px;height:24px;border-radius:50%;border:1px solid #d4d4d4}
.base-rule{width:700px;height:1px;margin:15px auto 0;background:linear-gradient(90deg,transparent,#b5b5b5,transparent)}
.copyright{display:flex;justify-content:center;align-items:center;gap:6px;margin-top:11px;font-size:8px;line-height:11px}
.copyright .sq{width:12px;height:12px;background:#ddd}
.chat-now{left:929px;top:1184px;width:132px;height:16px;background:var(--teal);color:var(--white);font-size:8px;font-weight:700;padding:3px 0 0 10px}
</style>
</head>
<body>
<div class="page">

  <div class="abs account-pill"><span>SIGN UP</span><span>LOGIN</span></div>
  <div class="abs brand">
    <span class="brand-mark"></span>
    <span class="brand-name">QUELLORY</span>
  </div>
  <div class="abs head-contact">
    <span class="round-icon"><svg width="12" height="10" viewBox="0 0 12 10"><path d="M1 1h10v6H5l-3 2V7H1z" fill="#3dd0c1"/></svg></span>
    <span>LIVE CHAT</span>
    <span class="round-icon" style="margin-left:8px"><svg width="11" height="11" viewBox="0 0 24 24"><path d="M6.6 10.8a15 15 0 006.6 6.6l2.2-2.2c.3-.3.7-.4 1-.2 1.1.4 2.3.6 3.6.6.6 0 1 .4 1 1V20c0 .6-.4 1-1 1A17 17 0 013 4c0-.6.4-1 1-1h3.5c.6 0 1 .4 1 1 0 1.3.2 2.5.6 3.6.1.3 0 .7-.2 1z" fill="#3dd0c1"/></svg></span>
    <span class="head-phone">555-010-4200</span>
  </div>
  <div class="abs header-rule"></div>
  <nav class="abs nav">
    <span>SERVERS</span><span>WORKSTATIONS</span><span>COMPONENTS</span><span>VIRTUAL REALITY</span><span>DRONES</span><span>ABOUT US</span><span>BLOG</span><span>RESOURCES</span><span>CONTACT US</span>
  </nav>
  <div class="abs search">Search<svg width="10" height="10" viewBox="0 0 10 10"><circle cx="4" cy="4" r="3" stroke="#3dd0c1" stroke-width="1.5" fill="none"/><path d="M6.2 6.2L9 9" stroke="#3dd0c1" stroke-width="1.5"/></svg></div>
  <div class="abs cart"><svg width="12" height="10" viewBox="0 0 12 10"><path d="M1 3h10l-1.5 6h-7z" fill="#3dd0c1"/><path d="M3 3l2-2.5M9 3L7 .5" stroke="#3dd0c1"/></svg></div>
  <div class="abs crumb"><b>HOME</b> / CONTACT US</div>

  <h1 class="abs page-title">CONTACT US</h1>

  <div class="abs map" role="img" aria-label="Street map of the area around the office headquarters"></div>
  <div class="abs map-river"></div>
  <div class="abs map-popup"><strong>OFFICE HEADQUARTERS</strong>QUELLORY SYSTEMS, LLC.<br>4820 ALDER AVE.<br>WESTBROOK, CA 90000</div>
  <svg class="abs map-pin" width="13" height="28" viewBox="0 0 13 28"><path d="M6.5 0A6.5 6.5 0 000 6.5C0 11 6.5 20 6.5 20S13 11 13 6.5A6.5 6.5 0 006.5 0z" fill="#d32f2f"/><circle cx="6.5" cy="22" r="1.5" fill="#b0202a"/></svg>
  <div class="abs map-pin-label">4820 Alder Avenue</div>

  <section class="abs hours">
    <h2 class="section-head">HOURS OF OPERATION</h2>
    <div class="hours-list">
      <div class="hour-row"><svg width="9" height="9" viewBox="0 0 10 10"><circle cx="5" cy="5" r="4" fill="none" stroke="#333" stroke-width="1.3"/><path d="M5 3v2h2" stroke="#333" fill="none"/></svg>Monday<span class="dots" style="width:116px"></span>8:00am- 5:00pm</div>
      <div class="hour-row"><svg width="9" height="9" viewBox="0 0 10 10"><circle cx="5" cy="5" r="4" fill="none" stroke="#333" stroke-width="1.3"/><path d="M5 3v2h2" stroke="#333" fill="none"/></svg>Tuesday<span class="dots" style="width:113px"></span>8:00am- 5:00pm</div>
      <div class="hour-row"><svg width="9" height="9" viewBox="0 0 10 10"><circle cx="5" cy="5" r="4" fill="none" stroke="#333" stroke-width="1.3"/><path d="M5 3v2h2" stroke="#333" fill="none"/></svg>Wednesday<span class="dots" style="width:116px"></span>8:00am- 5:00pm</div>
      <div class="hour-row"><svg width="9" height="9" viewBox="0 0 10 10"><circle cx="5" cy="5" r="4" fill="none" stroke="#333" stroke-width="1.3"/><path d="M5 3v2h2" stroke="#333" fill="none"/></svg>Thursday<span class="dots" style="width:116px"></span>8:00am- 5:00pm</div>
      <div class="hour-row"><svg width="9" height="9" viewBox="0 0 10 10"><circle cx="5" cy="5" r="4" fill="none" stroke="#333" stroke-width="1.3"/><path d="M5 3v2h2" stroke="#333" fill="none"/></svg>Friday<span class="dots" style="width:116px"></span>8:00am- 5:00pm</div>
    </div>
    <p class="hours-note">Our dedicated customer service representatives are available <span class="badge24">24</span></p>
  </section>
  <section class="abs connect">
    <h2 class="section-head">STAY CONNECTED</h2>
    <div class="social-dark"><span></span><span></span><span></span><span></span></div>
  </section>

  <section class="abs touch">
    <h2 class="section-head">GET IN TOUCH</h2>
    <div class="field-row">
      <div class="field"><label>NAME<i>*</i></label><div class="box"></div></div>
      <div class="field"><label>EMAIL<i>*</i></label><div class="box"></div></div>
      <div class="field"><label>PHONE<i>*</i></label><div class="box"></div></div>
    </div>
    <div class="message"><label>MESSAGE<i>*</i></label><div class="box"></div></div>
    <div class="send">SEND</div>
  </section>

  <div class="abs card" style="left:54px">
    <div class="card-icon"><svg width="52" height="46" viewBox="0 0 52 46"><path d="M2 2h48v30H12L2 44z" fill="none" stroke="#333" stroke-width="2.5"/><text x="26" y="24" font-size="17" font-weight="700" text-anchor="middle" fill="#333" font-family="Arimo,sans-serif">?</text></svg></div>
    <div class="card-body"><h3>GENERAL INQUIRIES</h3>
      <div class="card-line"><span class="dot-icon"><svg width="9" height="9" viewBox="0 0 24 24"><path d="M6.6 10.8a15 15 0 006.6 6.6l2.2-2.2c.3-.3.7-.4 1-.2 1.1.4 2.3.6 3.6.6.6 0 1 .4 1 1V20c0 .6-.4 1-1 1A17 17 0 013 4c0-.6.4-1 1-1h3.5c.6 0 1 .4 1 1 0 1.3.2 2.5.6 3.6z" fill="#fff"/></svg></span>(555)010-4200</div>
      <div class="card-line"><span class="dot-icon"><svg width="9" height="7" viewBox="0 0 9 7"><rect width="9" height="7" fill="#fff"/><path d="M0 0l4.5 4L9 0" stroke="#555" fill="none"/></svg></span>info@quellory.com</div>
    </div>
  </div>
  <div class="abs card" style="left:412px">
    <div class="card-icon"><svg width="52" height="46" viewBox="0 0 52 46"><path d="M2 2h48v30H12L2 44z" fill="none" stroke="#333" stroke-width="2.5"/><path d="M14 26l9-9 5 4 9-9" stroke="#333" stroke-width="2" fill="none"/><path d="M33 11h5v5" stroke="#333" stroke-width="2" fill="none"/></svg></div>
    <div class="card-body"><h3>SALES INQUIRIES</h3>
      <div class="card-line"><span class="dot-icon"><svg width="9" height="9" viewBox="0 0 24 24"><path d="M6.6 10.8a15 15 0 006.6 6.6l2.2-2.2c.3-.3.7-.4 1-.2 1.1.4 2.3.6 3.6.6.6 0 1 .4 1 1V20c0 .6-.4 1-1 1A17 17 0 013 4c0-.6.4-1 1-1h3.5c.6 0 1 .4 1 1 0 1.3.2 2.5.6 3.6z" fill="#fff"/></svg></span>(555)010-4200</div>
      <div class="card-line"><span class="dot-icon"><svg width="9" height="7" viewBox="0 0 9 7"><rect width="9" height="7" fill="#fff"/><path d="M0 0l4.5 4L9 0" stroke="#555" fill="none"/></svg></span>sales@quellory.com</div>
    </div>
  </div>
  <div class="abs card" style="left:767px">
    <div class="card-icon"><svg width="52" height="46" viewBox="0 0 52 46"><path d="M2 2h48v30H12L2 44z" fill="none" stroke="#333" stroke-width="2.5"/><path d="M16 13h20l-3 11H19z" fill="none" stroke="#333" stroke-width="2"/><path d="M20 13l4-5M32 13l-4-5" stroke="#333" stroke-width="1.5"/></svg></div>
    <div class="card-body"><h3>PURCHASING INQUIRIES</h3>
      <div class="card-line"><span class="dot-icon"><svg width="9" height="9" viewBox="0 0 24 24"><path d="M6.6 10.8a15 15 0 006.6 6.6l2.2-2.2c.3-.3.7-.4 1-.2 1.1.4 2.3.6 3.6.6.6 0 1 .4 1 1V20c0 .6-.4 1-1 1A17 17 0 013 4c0-.6.4-1 1-1h3.5c.6 0 1 .4 1 1 0 1.3.2 2.5.6 3.6z" fill="#fff"/></svg></span>(555)010-4201</div>
      <div class="card-line"><span class="dot-icon"><svg width="9" height="7" viewBox="0 0 9 7"><rect width="9" height="7" fill="#fff"/><path d="M0 0l4.5 4L9 0" stroke="#555" fill="none"/></svg></span>buy@quellory.com</div>
    </div>
  </div>

  <footer class="abs footer">
    <p class="footer-about">Based in Westbrook California, Quellory offers custom servers, storage, and workstations for local businesses in Los Angeles, Beverly Hills, Thousand Oaks, Ventura, Orange County, Santa Barbara, Oxnard, Irvine, Anaheim, and San Diego. Quellory also offers such products to clients throughout the United States and Worldwide.</p>
    <div class="footer-rule"></div>
    <div class="abs footer-contact">
      <div style="width:166px"><svg width="7" height="10" viewBox="0 0 7 10"><path d="M3.5 0A3.5 3.5 0 000 3.5C0 6 3.5 10 3.5 10S7 6 7 3.5A3.5 3.5 0 003.5 0z" fill="#fff"/></svg><span>4820 Alder Ave.<br>Westbrook, CA 90000</span></div>
      <div style="width:143px"><svg width="9" height="9" viewBox="0 0 24 24"><path d="M6.6 10.8a15 15 0 006.6 6.6l2.2-2.2c.3-.3.7-.4 1-.2 1.1.4 2.3.6 3.6.6.6 0 1 .4 1 1V20c0 .6-.4 1-1 1A17 17 0 013 4c0-.6.4-1 1-1h3.5c.6 0 1 .4 1 1 0 1.3.2 2.5.6 3.6z" fill="#fff"/></svg><span>555-010-4200</span></div>
      <div><svg width="9" height="7" viewBox="0 0 9 7"><rect width="9" height="7" fill="#fff"/><path d="M0 0l4.5 4L9 0" stroke="#a7a7a7" fill="none"/></svg><span>sales@quellory.com</span></div>
    </div>
    <div class="abs footer-links">
      <span style="width:143px">Computer Hardware</span>
      <span style="width:70px">Drones</span>
      <span style="width:107px">Virtual Reality</span>
      <span style="width:98px">About Us</span>
      <div><span>Customer Support</span><div class="sub">Terms and Conditions<br>Warranty Information<br>Contact Us<br>Return Policy</div></div>
    </div>
  </footer>
  <div class="abs footer-base">
    <div class="social-outline"><span></span><span></span><span></span><span></span></div>
    <div class="base-rule"></div>
    <div class="copyright"><span class="sq"></span><span>Quellory Systems, LLC.<br>Copyright © 2017</span></div>
  </div>
  <div class="abs chat-now">CHAT NOW</div>
</div>
</body>
</html>
```